stationary for a modern hotel
Venmiro Hotels
Project: stationary for a modern hotel
stationary for a modern hotel - Hospitality Industry
Creative Brief
Use same font as used in my logo
anything that can go very well with my logo
Simple
Tundeyemi Okafordike
G.M
Venmiro Hotels Plot 318,Adebanjo-Ekwueme Way,Garki District Abuja Nigeria
tunde@venmirohotels.com
www.venmirohotels.com

```html
<!DOCTYPE html>
<html lang="en">
<head>
<meta charset="utf-8">
<title>Venmiro Hotels – Business Card</title>
<link rel="stylesheet" href="https://fonts.googleapis.com/css2?family=Questrial&display=swap">
<style>
  :root {
    --card-bg: #ffffff;
    --brand-gold: #8a6a3c;
    --name-brown: #5a2d0c;
    --title-red: #8b2a12;
    --text-grey: #6b5a4c;
    --band-tan: #b58a52;
    --band-red: #7a1416;
    --band-text: #ffffff;
  }
  * { margin: 0; padding: 0; box-sizing: border-box; }
  html, body {
    width: 1200px;
    height: 778px;
    overflow: hidden;
    background: var(--card-bg);
  }
  .business-card {
    position: relative;
    width: 1200px;
    height: 778px;
    background: var(--card-bg);
    font-family: "Questrial", sans-serif;
    text-align: center;
  }
  .brand-name {
    position: absolute;
    top: 140px;
    left: 0;
    width: 100%;
    font-size: 66px;
    letter-spacing: 4px;
    color: var(--brand-gold);
    text-transform: uppercase;
    font-weight: 400;
  }
  .person-name {
    position: absolute;
    top: 368px;
    left: 0;
    width: 100%;
    font-size: 44px;
    color: var(--name-brown);
  }
  .person-title {
    position: absolute;
    top: 428px;
    left: 0;
    width: 100%;
    font-size: 42px;
    color: var(--title-red);
  }
  .company {
    position: absolute;
    top: 506px;
    left: 0;
    width: 100%;
    font-size: 31px;
    color: var(--name-brown);
  }
  .address {
    position: absolute;
    top: 548px;
    left: 0;
    width: 100%;
    font-size: 27px;
    color: var(--text-grey);
  }
  .contact-row {
    position: absolute;
    top: 596px;
    left: 0;
    width: 100%;
    display: flex;
    justify-content: center;
    gap: 36px;
    font-size: 27px;
    color: var(--text-grey);
  }
  .contact-item { display: flex; align-items: center; gap: 8px; }
  .contact-icon { width: 24px; height: 24px; fill: var(--title-red); }
  .footer-band {
    position: absolute;
    left: 0;
    top: 652px;
    width: 1200px;
    height: 64px;
  }
  .website {
    position: absolute;
    top: 664px;
    right: 60px;
    font-size: 31px;
    letter-spacing: 2px;
    color: var(--band-text);
  }
</style>
</head>
<body>
  <main class="business-card">
    <div class="brand-name">Venmiro Hotels</div>

    <div class="person-name">Tundeyemi Okafordike</div>
    <div class="person-title">G.M</div>
    <div class="company">Venmiro Hotels</div>
    <div class="address">Plot 318, Adebanjo-Ekwueme Way, Garki District, Abuja, Nigeria</div>

    <div class="contact-row">
      <span class="contact-item">
        <svg class="contact-icon" viewBox="0 0 24 24" aria-hidden="true">
          <path d="M6.6 10.8a15.1 15.1 0 0 0 6.6 6.6l2.2-2.2a1 1 0 0 1 1-.25 11.4 11.4 0 0 0 3.6.57 1 1 0 0 1 1 1V20a1 1 0 0 1-1 1A17 17 0 0 1 3 4a1 1 0 0 1 1-1h3.5a1 1 0 0 1 1 1c0 1.25.2 2.45.57 3.57a1 1 0 0 1-.25 1z"/>
        </svg>
        +2348105550147
      </span>
      <span class="contact-item">
        <svg class="contact-icon" viewBox="0 0 24 24" aria-hidden="true">
          <path d="M8 2h8a2 2 0 0 1 2 2v16a2 2 0 0 1-2 2H8a2 2 0 0 1-2-2V4a2 2 0 0 1 2-2zm0 3v13h8V5zm4 14.2a.9.9 0 1 0 0 1.8.9.9 0 0 0 0-1.8z"/>
        </svg>
        +2348105550147
      </span>
      <span class="contact-item">
        <svg class="contact-icon" viewBox="0 0 24 24" aria-hidden="true">
          <path d="M3 5h18a1 1 0 0 1 1 1v12a1 1 0 0 1-1 1H3a1 1 0 0 1-1-1V6a1 1 0 0 1 1-1zm1 2.2V17h16V7.2l-8 5.3zM5.2 7 12 11.5 18.8 7z"/>
        </svg>
        tunde@venmirohotels.com
      </span>
    </div>

    <svg class="footer-band" viewBox="0 0 1200 64" aria-hidden="true">
      <polygon points="0,0 710,0 672,64 0,64" fill="var(--band-tan)"/>
      <polygon points="728,0 1200,0 1200,64 690,64" fill="var(--band-red)"/>
    </svg>
    <div class="website">www.venmirohotels.com</div>
  </main>
</body>
</html>
```